Vexla.IO Portal Application Design

** See the attached treatment PDF document with complete details, but here are the broad points:**

We need designs for a login screen and three very similar interior page screens. Because the app requires a CodeNest, RepoDen or Forkmoor account to login, screen shots are attached to this treatment. Please review those for the designs needed.
- Login Page
- Project Index page (with sidebar tabs for other options. Those specific pages do not need to be coded once we have the template).
- Project build list. A list of the builds available per project
- Build details. This shows the build steps and results of the build steps.

The site should be visually compatible with https://vexlasite.examplehost.net. The same logo and color scheme (logo attached)

General templates are desired that we can build on.

There is a significant bonus tip involved if you’re willing to provide a toggle for a light and a dark mode. I do not know what this would look like but feel free to present proposals.

Industry/Entity Type

Continuous Integration/Testing (think LoopRun, MarlowCI)

Coding

Coded - Design and coding required

Number of Pages Required

1 page

Font styles to use
Sans Serif
Other font styles liked:
• Roboto

Colors
0054AA
0677BA
7BADD7
CADEEF
E8F1F8
FFC000
F8CF3A
FAE287
FDF2CF
FEFAEE

Requirements
Nice to have
• Light and Dark Mode

```html
<!DOCTYPE html>
<html lang="en">
<head>
<meta charset="utf-8">
<title>Vexla.IO Portal – Light and Dark Templates</title>
<link rel="stylesheet" href="https://fonts.googleapis.com/css2?family=Roboto:wght@300;400;500;700&display=swap">
<style>
:root{
  --yellow:#f5b318;--navy:#0b2041;--slate:#313a57;--steel:#5d5f78;--haze:#9a99ab;--mist:#e1e0e7;--snow:#f7f8f9;--white:#ffffff;
  --board:#cfcfcf;
}
*{box-sizing:border-box;margin:0;padding:0}
html,body{width:915px;height:1200px;overflow:hidden;background:var(--board)}
body{font-family:"Roboto",Arial,sans-serif;color:var(--navy)}
.board{position:absolute;left:0;top:0;width:1680px;height:2203px;transform:scale(.54464);transform-origin:0 0;background:var(--board)}
.abs{position:absolute}

/* style guide header */
.brand-mark{left:520px;top:150px;display:flex;align-items:center;gap:10px;font-size:22px;font-weight:500;color:var(--slate)}
.brand-mark .dot{width:40px;height:40px;border-radius:50%;background:var(--steel)}
.guide-title{font-size:30px;font-weight:400;color:var(--slate)}
.guide-sub{font-size:22px;font-weight:300;color:var(--steel)}
.swatches{left:898px;top:166px;display:flex;gap:1px}
.swatch{width:36px;display:flex;flex-direction:column;align-items:center;gap:7px;font-size:7px;color:var(--slate);white-space:nowrap}
.swatch i{display:block;width:30px;height:30px;border-radius:50%}

/* login */
.login{width:522px;height:335px;border-radius:6px;overflow:hidden;background:linear-gradient(180deg,#1d3868 0%,#15305c 55%,#0f2650 100%);display:flex;flex-direction:column;align-items:center;color:var(--white)}
.login .pattern{position:absolute;inset:0}
.login .dot{margin-top:126px;width:16px;height:16px;border-radius:50%;background:var(--haze);position:relative}
.login h1{margin-top:14px;font-size:17px;font-weight:500;position:relative}
.login .providers{margin-top:12px;display:flex;gap:5px;position:relative}
.provider{height:17px;padding:0 9px;border-radius:3px;background:#2c4474;font-size:5px;display:flex;align-items:center;gap:3px}
.provider i{width:5px;height:5px;border-radius:50%;background:var(--white)}

.caption{font-size:17px;color:var(--slate)}

/* app screens */
.light{--side:#ffffff;--main:#f1f1f1;--card:#ffffff;--ink:#0b2041;--muted:#9a99ab;--line:#e4e3e9;--log:#f7f8f9;--active:#ffffff;--btn-line:#f5b318;--x:#f5b318}
.dark{--side:#0a1c3a;--main:#0b2041;--card:#10294f;--ink:#ffffff;--muted:#8d90a8;--line:#1b3663;--log:#0b2041;--active:#10294f;--btn-line:#ffffff;--x:#ffffff}
.screen{width:668px;height:428px;border-radius:8px;overflow:hidden;display:flex;color:var(--ink);background:var(--main)}
.side{width:116px;background:var(--side);position:relative;flex:none}
.dark .side{border-right:1px solid #0e2650}
.side .brand{position:absolute;left:10px;top:10px;right:8px;display:flex;align-items:center;gap:5px;font-size:8px;font-weight:700}
.side .brand .dot{width:16px;height:16px;border-radius:50%;background:var(--haze)}
.side .brand svg{margin-left:auto;width:6px;height:6px}
.nav{position:absolute;left:9px;right:9px;top:56px;list-style:none}
.nav li{height:20px;display:flex;align-items:center;gap:6px;padding-left:10px;font-size:6px;font-weight:500;margin-bottom:2px;color:var(--ink)}
.dark .nav li{color:#b5b8cc}
.nav li svg{width:8px;height:8px}
.nav li.on{background:var(--active);border-left:2px solid var(--yellow);box-shadow:0 1px 6px rgba(11,32,65,.12);margin-bottom:6px;padding-left:8px}
.dark .nav li.on{color:#fff;box-shadow:none}
.usage{position:absolute;left:9px;right:9px;bottom:14px;font-size:5px}
.usage .bar{height:3px;border-radius:2px;background:var(--line);margin-bottom:7px}
.usage .bar b{display:block;width:22%;height:100%;border-radius:2px;background:var(--navy)}
.dark .usage .bar b{background:#fff}
.usage .row{display:flex;align-items:center;justify-content:space-between}
.pill-upgrade{background:var(--yellow);color:var(--navy);border-radius:6px;padding:2px 6px;font-weight:700}
.main{flex:1;position:relative}
.topbar{height:33px;border-bottom:1px solid var(--line);display:flex;align-items:center;padding:0 19px 0 19px;font-size:5px}
.topbar .mode{width:9px;height:9px}
.topbar .user{margin-left:auto;display:flex;align-items:center;gap:4px;color:var(--muted)}
.topbar .user i{width:9px;height:9px;border-radius:50%;background:var(--steel)}
.page-head{position:absolute;left:19px;right:19px;top:48px;display:flex;align-items:flex-start}
.page-head h2{font-size:12px;font-weight:500}
.crumbs{font-size:6px;color:var(--muted);margin-top:4px}
.crumbs b{color:var(--ink);font-weight:400}
.views{margin-left:auto;display:flex;gap:6px;margin-top:4px}
.views svg{width:9px;height:9px}

/* project cards */
.projects{position:absolute;left:19px;top:82px;display:grid;grid-template-columns:252px 252px;gap:9px}
.project{height:112px;background:var(--card);border-radius:6px;padding:14px 17px}
.light .project{box-shadow:0 1px 4px rgba(11,32,65,.05)}
.project h3{font-size:8.5px;font-weight:500;display:flex;align-items:center;gap:3px}
.project h3 i{width:5px;height:6px;background:var(--muted);border-radius:1px}
.project .upd{font-size:5px;color:var(--muted);margin:2px 0 0 9px}
.stats{display:flex;margin-top:11px}
.stat{display:flex;align-items:center;gap:5px;font-size:5px;color:var(--muted);width:86px}
.stat:first-child{width:78px}
.stat svg{width:13px;height:13px;flex:none}
.stat b{display:block;color:var(--ink);font-size:6px;font-weight:500;margin-top:1px}
.btn{display:inline-flex;align-items:center;justify-content:center;height:17px;border-radius:9px;font-size:6px;font-weight:500}
.btn-fill{background:var(--yellow);color:var(--navy);width:70px}
.project .btn{margin-top:11px}
.btn-line{border:1px solid var(--btn-line);color:var(--ink);width:70px}

/* builds */
.search{position:absolute;left:211px;top:53px;width:115px;height:20px;background:var(--card);border-radius:3px;font-size:5px;color:var(--muted);display:flex;align-items:center;padding:0 7px}
.search svg{margin-left:auto;width:7px;height:7px}
.showall{position:absolute;right:19px;top:56px;display:flex;align-items:center;gap:6px;font-size:5px}
.toggle{width:27px;height:14px;border-radius:7px;background:var(--card);border:1px solid var(--line);position:relative}
.toggle i{position:absolute;left:2px;top:2px;width:9px;height:9px;border-radius:50%;background:var(--mist)}
.dark .toggle{background:#0b2041;border-color:#fff}
.dark .toggle i{background:#fff;left:2px}
.builds{position:absolute;left:19px;right:19px;top:94px}
.build{height:68px;background:var(--card);border-radius:6px;margin-bottom:9px;display:flex;align-items:center;padding:0 17px}
.build .info{width:260px}
.build h3{font-size:8.5px;font-weight:500}
.date{display:inline-block;margin-top:4px;border:1px solid var(--muted);border-radius:4px;padding:1px 4px;font-size:4.5px}
.acts{margin-top:5px;display:flex;gap:6px;font-size:5px}
.acts span{display:flex;align-items:center;gap:2px}
.acts svg{width:5px;height:5px}
.vsep{width:1px;height:34px;background:var(--line)}
.disk{display:flex;align-items:center;gap:7px;font-size:5px;color:var(--muted);width:122px;padding-left:16px}
.disk svg{width:13px;height:13px}
.disk b{display:block;color:var(--ink);font-weight:500;font-size:5.5px;margin-top:1px}
.build .cta{margin-left:auto;display:flex;flex-direction:column;align-items:center;gap:5px;font-size:5px}
.build .cta span{display:flex;align-items:center;gap:3px}
.build .cta svg{width:6px;height:6px}

/* build details */
.detail-head{position:absolute;left:19px;right:19px;top:90px;border-top:1px solid var(--line);border-bottom:1px solid var(--line);height:68px;display:flex;align-items:center}
.detail-head .info{width:212px}
.detail-head h3{font-size:8px;font-weight:500}
.detail-head .disk{width:128px}
.detail-head .btn-fill{width:48px;height:16px}
.adv{margin-left:auto;font-size:6px;font-weight:500;padding-left:14px;display:flex;align-items:center;gap:4px}
.detail-head .vsep{margin-left:20px}
.tasks{position:absolute;left:19px;right:19px;top:177px}
.task{background:var(--card);border-radius:6px;margin-bottom:9px;overflow:hidden}
.task .th{height:47px;display:flex;align-items:center;padding:0 17px}
.task h4{font-size:7.5px;font-weight:500}
.task .dur{font-size:5px;margin-top:3px;display:flex;align-items:center;gap:3px;color:var(--ink)}
.dark .task .dur{color:var(--muted)}
.task .dur b{font-weight:500}
.task .dur svg{width:6px;height:6px}
.task .tog{margin-left:auto;width:18px;height:18px;border-radius:50%;border:1px solid var(--yellow);color:var(--yellow);font-size:10px;display:flex;align-items:center;justify-content:center;font-weight:300}
.task .tog.x{border-color:var(--x);color:var(--x);font-size:9px}
.light .task .tog.x{border-color:var(--mist);color:var(--yellow)}
.log{background:var(--log);border:1px solid var(--line);border-top:0;border-radius:0 0 6px 6px;padding:7px 17px 7px 20px;font-size:6px;line-height:10px;list-style:none}
.dark .log{background:#0d2448;border:0}
</style>
</head>
<body>
<svg width="0" height="0" style="position:absolute" aria-hidden="true">
  <defs>
    <symbol id="i-disk" viewBox="0 0 16 16"><rect x="1.5" y="3" width="13" height="10" rx="1.5" fill="none" stroke="currentColor" stroke-width="1.1"/><line x1="1.5" y1="9.5" x2="14.5" y2="9.5" stroke="currentColor" stroke-width="1.1"/><circle cx="4.5" cy="11.3" r=".6" fill="currentColor"/><circle cx="6.5" cy="11.3" r=".6" fill="currentColor"/></symbol>
    <symbol id="i-clock" viewBox="0 0 16 16"><circle cx="8" cy="8" r="6.5" fill="none" stroke="currentColor" stroke-width="1.1"/><path d="M8 4v4.3l2.6 1.6" fill="none" stroke="currentColor" stroke-width="1.1"/></symbol>
    <symbol id="i-branch" viewBox="0 0 16 16"><circle cx="5" cy="3" r="1.6" fill="none" stroke="currentColor" stroke-width="1.1"/><circle cx="5" cy="13" r="1.6" fill="none" stroke="currentColor" stroke-width="1.1"/><circle cx="11" cy="5" r="1.6" fill="none" stroke="currentColor" stroke-width="1.1"/><path d="M5 4.6v6.8M11 6.6c0 3-6 2-6 4.8" fill="none" stroke="currentColor" stroke-width="1.1"/></symbol>
    <symbol id="i-moon" viewBox="0 0 16 16"><path d="M10.5 2.5A6 6 0 1 0 13.5 11 5 5 0 0 1 10.5 2.5z" fill="none" stroke="currentColor" stroke-width="1.2"/></symbol>
    <symbol id="i-sun" viewBox="0 0 16 16"><circle cx="8" cy="8" r="3" fill="none" stroke="currentColor" stroke-width="1.1"/><path d="M8 1v2M8 13v2M1 8h2M13 8h2M3 3l1.4 1.4M11.6 11.6 13 13M3 13l1.4-1.4M11.6 4.4 13 3" stroke="currentColor" stroke-width="1.1"/></symbol>
    <symbol id="i-grid" viewBox="0 0 16 16"><g fill="none" stroke="currentColor" stroke-width="1.2"><rect x="2" y="2" width="5" height="5"/><rect x="9" y="2" width="5" height="5"/><rect x="2" y="9" width="5" height="5"/><rect x="9" y="9" width="5" height="5"/></g></symbol>
    <symbol id="i-list" viewBox="0 0 16 16"><path d="M2 3h1M5 3h9M2 8h1M5 8h9M2 13h1M5 13h9" stroke="currentColor" stroke-width="1.2"/></symbol>
    <symbol id="i-search" viewBox="0 0 16 16"><circle cx="7" cy="7" r="4.5" fill="none" stroke="currentColor" stroke-width="1.4"/><path d="M10.5 10.5 14 14" stroke="currentColor" stroke-width="1.4"/></symbol>
    <symbol id="i-chev" viewBox="0 0 16 16"><path d="M10 3 5 8l5 5" fill="none" stroke="currentColor" stroke-width="1.8"/></symbol>
    <symbol id="i-stack" viewBox="0 0 16 16"><path d="M8 2 14 5 8 8 2 5zM2 8l6 3 6-3M2 11l6 3 6-3" fill="none" stroke="currentColor" stroke-width="1.2"/></symbol>
    <symbol id="i-user" viewBox="0 0 16 16"><circle cx="8" cy="5" r="3" fill="none" stroke="currentColor" stroke-width="1.2"/><path d="M2.5 15c0-3.3 2.5-5 5.5-5s5.5 1.7 5.5 5" fill="none" stroke="currentColor" stroke-width="1.2"/></symbol>
    <symbol id="i-globe" viewBox="0 0 16 16"><circle cx="8" cy="8" r="6.5" fill="none" stroke="currentColor" stroke-width="1.1"/><path d="M1.5 8h13M8 1.5c-3 3.5-3 9.5 0 13M8 1.5c3 3.5 3 9.5 0 13" fill="none" stroke="currentColor" stroke-width="1.1"/></symbol>
    <symbol id="i-card" viewBox="0 0 16 16"><rect x="1.5" y="3.5" width="13" height="9" rx="1" fill="none" stroke="currentColor" stroke-width="1.1"/><path d="M1.5 6.5h13" stroke="currentColor" stroke-width="1.1"/></symbol>
    <symbol id="i-hist" viewBox="0 0 16 16"><path d="M2.5 8a5.5 5.5 0 1 0 1.6-3.9M2 2.5v2.5h2.5M8 5v3.3l2 1.2" fill="none" stroke="currentColor" stroke-width="1.1"/></symbol>
    <symbol id="i-upload" viewBox="0 0 16 16"><rect x="1.5" y="2.5" width="13" height="11" rx="1.5" fill="none" stroke="currentColor" stroke-width="1.1"/><path d="M8 11V5.5M5.5 8 8 5.5 10.5 8" fill="none" stroke="currentColor" stroke-width="1.1"/></symbol>
    <symbol id="i-rebuild" viewBox="0 0 16 16"><path d="M2 5h9l-3-3M14 11H5l3 3" fill="none" stroke="currentColor" stroke-width="1.6"/></symbol>
    <symbol id="i-pin" viewBox="0 0 16 16"><path d="M9 1.5 14.5 7l-2 .5-3 3 .5 3L8 15 1 8l1.5-2 3 .5 3-3z" fill="none" stroke="currentColor" stroke-width="1.4"/></symbol>
    <symbol id="i-trash" viewBox="0 0 16 16"><path d="M2.5 4h11M6 4V2h4v2M4 4l1 10h6l1-10" fill="none" stroke="currentColor" stroke-width="1.4"/></symbol>
    <symbol id="i-pr" viewBox="0 0 16 16"><path d="M8 1v14M3 5l5-4 5 4M3 11l5 4 5-4" fill="none" stroke="currentColor" stroke-width="1.6"/></symbol>
    <symbol id="i-code" viewBox="0 0 16 16"><path d="M5 4 1 8l4 4M11 4l4 4-4 4M9.5 2.5 6.5 13.5" fill="none" stroke="currentColor" stroke-width="1.5"/></symbol>
  </defs>
</svg>

<div class="board">

  <!-- style guide -->
  <div class="abs brand-mark"><span class="dot"></span>Vexla.IO</div>
  <div class="abs guide-title" style="left:718px;top:132px">Fonts:</div>
  <div class="abs guide-sub" style="left:719px;top:166px">Roboto</div>
  <div class="abs guide-title" style="left:900px;top:134px">Colors:</div>
  <div class="abs swatches">
    <div class="swatch"><i style="background:#f5b318"></i>#f5b318</div>
    <div class="swatch"><i style="background:#0b2041"></i>#0b2041</div>
    <div class="swatch"><i style="background:#313a57"></i>#313a57</div>
    <div class="swatch"><i style="background:#5d5f78"></i>#5d5f78</div>
    <div class="swatch"><i style="background:#9a99ab"></i>#9a99ab</div>
    <div class="swatch"><i style="background:#e1e0e7"></i>#e1e0e7</div>
    <div class="swatch"><i style="background:#ffffff"></i>#f7f8f9</div>
  </div>

  <!-- login screens -->
  <section class="abs login" style="left:196px;top:260px">
    <div class="pattern" role="img" aria-label="Soft navy geometric backdrop"></div>
    <div class="dot"></div>
    <h1>Sign in to Vexla.IO</h1>
    <div class="providers">
      <span class="provider"><i></i>Sign with CodeNest</span>
      <span class="provider"><i></i>Sign with Forkmoor</span>
      <span class="provider"><i></i>Sign with RepoDen</span>
    </div>
  </section>
  <section class="abs login" style="left:958px;top:260px">
    <div class="pattern" role="img" aria-label="Soft navy geometric backdrop"></div>
    <div class="dot"></div>
    <h1>Sign in to Vexla.IO</h1>
    <div class="providers">
      <span class="provider"><i></i>Sign with CodeNest</span>
      <span class="provider"><i></i>Sign with Forkmoor</span>
      <span class="provider"><i></i>Sign with RepoDen</span>
    </div>
  </section>

  <!-- ===== Index of Projects: light ===== -->
  <section class="abs screen light" style="left:123px;top:667px">
    <aside class="side">
      <div class="brand"><span class="dot"></span>Vexla.IO<svg><use href="#i-chev"/></svg></div>
      <ul class="nav">
        <li class="on"><svg><use href="#i-stack"/></svg>Projects</li>
        <li><svg><use href="#i-user"/></svg>Admins</li>
        <li><svg><use href="#i-globe"/></svg>Subscriptions</li>
        <li><svg><use href="#i-card"/></svg>Payment Method</li>
        <li><svg><use href="#i-hist"/></svg>Payment History</li>
      </ul>
      <div class="usage"><div class="bar"><b></b></div><div class="row">Using 8.6 GB of 500 GB<span class="pill-upgrade">Upgrade</span></div></div>
    </aside>
    <div class="main">
      <div class="topbar"><svg class="mode"><use href="#i-moon"/></svg><span class="user">Welcome, User<i></i></span></div>
      <div class="page-head"><h2>Projects overview</h2><div class="views"><svg><use href="#i-grid"/></svg><svg style="color:var(--muted)"><use href="#i-list"/></svg></div></div>
      <div class="projects">
        <article class="project"><h3><i></i>VexlaIO/vexla.io</h3><p class="upd">Last update: Nov 7, 2025</p>
          <div class="stats"><div class="stat"><svg><use href="#i-branch"/></svg><div>Created<b>09/25/25</b></div></div><div class="stat"><svg><use href="#i-disk"/></svg><div>Used disk space<b>627.0 MB</b></div></div><div class="stat"><svg><use href="#i-clock"/></svg><div>Average build time<b>10 minutes</b></div></div></div>
          <span class="btn btn-fill">View Project</span></article>
        <article class="project"><h3><i></i>VexlaIO/vexla_test</h3><p class="upd">Last update: Nov 1, 2025</p>
          <div class="stats"><div class="stat"><svg><use href="#i-branch"/></svg><div>Created<b>09/23/25</b></div></div><div class="stat"><svg><use href="#i-disk"/></svg><div>Used disk space<b>5.7 GB</b></div></div><div class="stat"><svg><use href="#i-clock"/></svg><div>Average build time<b>12 minutes</b></div></div></div>
          <span class="btn btn-fill">View Project</span></article>
        <article class="project"><h3><i></i>VexlaIO/vexla-demos</h3><p class="upd">Last update: Nov 7, 2025</p>
          <div class="stats"><div class="stat"><svg><use href="#i-branch"/></svg><div>Created<b>10/13/25</b></div></div><div class="stat"><svg><use href="#i-disk"/></svg><div>Used disk space<b>2.7 GB</b></div></div><div class="stat"><svg><use href="#i-clock"/></svg><div>Average build time<b>27 minutes</b></div></div></div>
          <span class="btn btn-fill">View Project</span></article>
      </div>
    </div>
  </section>

  <!-- ===== Index of Projects: dark ===== -->
  <section class="abs screen dark" style="left:884px;top:667px">
    <aside class="side">
      <div class="brand"><span class="dot"></span>Vexla.IO<svg><use href="#i-chev"/></svg></div>
      <ul class="nav">
        <li class="on"><svg><use href="#i-stack"/></svg>Projects</li>
        <li><svg><use href="#i-user"/></svg>Admins</li>
        <li><svg><use href="#i-globe"/></svg>Subscriptions</li>
        <li><svg><use href="#i-card"/></svg>Payment Method</li>
        <li><svg><use href="#i-hist"/></svg>Payment History</li>
      </ul>
      <div class="usage"><div class="bar"><b></b></div><div class="row">Using 8.6 GB of 500 GB<span class="pill-upgrade">Upgrade</span></div></div>
    </aside>
    <div class="main">
      <div class="topbar"><svg class="mode"><use href="#i-sun"/></svg><span class="user">Welcome, User<i></i></span></div>
      <div class="page-head"><h2>Projects overview</h2><div class="views"><svg><use href="#i-grid"/></svg><svg style="color:var(--muted)"><use href="#i-list"/></svg></div></div>
      <div class="projects">
        <article class="project"><h3><i></i>VexlaIO/vexla.io</h3><p class="upd">Last update: Nov 7, 2025</p>
          <div class="stats"><div class="stat"><svg><use href="#i-branch"/></svg><div>Created<b>09/25/25</b></div></div><div class="stat"><svg><use href="#i-disk"/></svg><div>Used disk space<b>627.0 MB</b></div></div><div class="stat"><svg><use href="#i-clock"/></svg><div>Average build time<b>10 minutes</b></div></div></div>
          <span class="btn btn-fill">View Project</span></article>
        <article class="project"><h3><i></i>VexlaIO/vexla_test</h3><p class="upd">Last update: Nov 1, 2025</p>
          <div class="stats"><div class="stat"><svg><use href="#i-branch"/></svg><div>Created<b>09/23/25</b></div></div><div class="stat"><svg><use href="#i-disk"/></svg><div>Used disk space<b>5.7 GB</b></div></div><div class="stat"><svg><use href="#i-clock"/></svg><div>Average build time<b>12 minutes</b></div></div></div>
          <span class="btn btn-fill">View Project</span></article>
        <article class="project"><h3><i></i>VexlaIO/vexla-demos</h3><p class="upd">Last update: Nov 7, 2025</p>
          <div class="stats"><div class="stat"><svg><use href="#i-branch"/></svg><div>Created<b>10/13/25</b></div></div><div class="stat"><svg><use href="#i-disk"/></svg><div>Used disk space<b>2.7 GB</b></div></div><div class="stat"><svg><use href="#i-clock"/></svg><div>Average build time<b>27 minutes</b></div></div></div>
          <span class="btn btn-fill">View Project</span></article>
      </div>
    </div>
  </section>

  <p class="abs caption" style="left:123px;top:1104px">Index of Projects</p>
  <p class="abs caption" style="left:884px;top:1104px">Index of Projects</p>

  <!-- ===== Index of Builds: light ===== -->
  <section class="abs screen light" style="left:123px;top:1140px">
    <aside class="side">
      <div class="brand"><span class="dot"></span>Vexla.IO<svg><use href="#i-chev"/></svg></div>
      <ul class="nav" style="top:46px">
        <li class="on"><svg><use href="#i-stack"/></svg>Builds</li>
        <li><svg><use href="#i-user"/></svg>Build Assets</li>
        <li><svg><use href="#i-upload"/></svg>Upload Tokens</li>
      </ul>
      <div class="usage"><div class="bar"><b></b></div><div class="row">Using 8.6 GB of 500 GB<span class="pill-upgrade">Upgrade</span></div></div>
    </aside>
    <div class="main">
      <div class="topbar"><svg class="mode"><use href="#i-moon"/></svg><span class="user">Welcome, User<i></i></span></div>
      <div class="page-head"><div><h2>Vexla_Test</h2><p class="crumbs">Vexla.IO &gt; <b>Builds</b></p></div></div>
      <div class="search">Search build...<svg><use href="#i-search"/></svg></div>
      <div class="showall">Show all builds<span class="toggle"><i></i></span></div>
      <div class="builds">
        <article class="build"><div class="info"><h3>Testing PHP 8.5 container</h3><span class="date">11/1/2025 6:50 PM</span>
          <div class="acts"><span><svg><use href="#i-rebuild"/></svg>Rebuild</span><span><svg><use href="#i-pin"/></svg>Pin</span><span><svg><use href="#i-trash"/></svg>Delete</span><span><svg><use href="#i-pr"/></svg>View pull requests</span><span><svg><use href="#i-rebuild"/></svg>View branch - Commit 6e2e</span></div></div>
          <div class="vsep"></div><div class="disk"><svg><use href="#i-disk"/></svg><div>Used Disk Space<b>627.0 MB</b></div></div><div class="vsep"></div>
          <div class="cta"><span class="btn btn-line">View Project</span><span><svg><use href="#i-hist"/></svg>View older versions</span></div></article>
        <article class="build"><div class="info"><h3>A test for our 5.6 image</h3><span class="date">10/7/2025 3:42 PM</span>
          <div class="acts"><span><svg><use href="#i-rebuild"/></svg>Rebuild</span><span><svg><use href="#i-pin"/></svg>Pin</span><span><svg><use href="#i-trash"/></svg>Delete</span><span><svg><use href="#i-pr"/></svg>View pull requests</span><span><svg><use href="#i-rebuild"/></svg>View branch - Commit 6e2e</span></div></div>
          <div class="vsep"></div><div class="disk"><svg><use href="#i-disk"/></svg><div>Used Disk Space<b>627.0 MB</b></div></div><div class="vsep"></div>
          <div class="cta"><span class="btn btn-line">View Project</span><span><svg><use href="#i-hist"/></svg>View older versions</span></div></article>
        <article class="build"><div class="info"><h3>Testing of PHP 7.0 Container</h3><span class="date">11/1/2025 6:50 PM</span>
          <div class="acts"><span><svg><use href="#i-rebuild"/></svg>Rebuild</span><span><svg><use href="#i-pin"/></svg>Pin</span><span><svg><use href="#i-trash"/></svg>Delete</span><span><svg><use href="#i-pr"/></svg>View pull requests</span><span><svg><use href="#i-rebuild"/></svg>View branch - Commit 6e2e</span></div></div>
          <div class="vsep"></div><div class="disk"><svg><use href="#i-disk"/></svg><div>Used Disk Space<b>627.0 MB</b></div></div><div class="vsep"></div>
          <div class="cta"><span class="btn btn-fill">View Project</span><span><svg><use href="#i-hist"/></svg>View older versions</span></div></article>
        <article class="build"><div class="info"><h3>A test for PHP 8.2</h3><span class="date">11/1/2025 6:50 PM</span>
          <div class="acts"><span><svg><use href="#i-rebuild"/></svg>Rebuild</span><span><svg><use href="#i-pin"/></svg>Pin</span><span><svg><use href="#i-trash"/></svg>Delete</span><span><svg><use href="#i-pr"/></svg>View pull requests</span><span><svg><use href="#i-rebuild"/></svg>View branch - Commit 6e2e</span></div></div>
          <div class="vsep"></div><div class="disk"><svg><use href="#i-disk"/></svg><div>Used Disk Space<b>627.0 MB</b></div></div><div class="vsep"></div>
          <div class="cta"><span class="btn btn-line">View Project</span><span><svg><use href="#i-hist"/></svg>View older versions</span></div></article>
        <article class="build"><div class="info"><h3>A test for PHP 8.2</h3><span class="date">11/1/2025 6:50 PM</span></div>
          <div class="vsep"></div><div class="disk"></div><div class="vsep"></div>
          <div class="cta"><span class="btn btn-line">View Project</span></div></article>
      </div>
    </div>
  </section>

  <!-- ===== Index of Builds: dark ===== -->
  <section class="abs screen dark" style="left:884px;top:1140px">
    <aside class="side">
      <div class="brand"><span class="dot"></span>Vexla.IO<svg><use href="#i-chev"/></svg></div>
      <ul class="nav">
        <li class="on"><svg><use href="#i-stack"/></svg>Builds</li>
        <li><svg><use href="#i-user"/></svg>Build Assets</li>
        <li><svg><use href="#i-upload"/></svg>Upload Tokens</li>
      </ul>
      <div class="usage"><div class="bar"><b></b></div><div class="row">Using 8.6 GB of 500 GB<span class="pill-upgrade">Upgrade</span></div></div>
    </aside>
    <div class="main">
      <div class="topbar"><svg class="mode"><use href="#i-sun"/></svg><span class="user">Welcome, User<i></i></span></div>
      <div class="page-head"><div><h2>Vexla_Test</h2><p class="crumbs">Vexla.IO &gt; <b>Builds</b></p></div></div>
      <div class="search">Search build...<svg><use href="#i-search"/></svg></div>
      <div class="showall"><span class="toggle"><i></i></span></div>
      <div class="builds">
        <article class="build"><div class="info"><h3>Testing PHP 8.5 container</h3><span class="date">11/1/2025 6:50 PM</span>
          <div class="acts"><span><svg><use href="#i-rebuild"/></svg>Rebuild</span><span><svg><use href="#i-pin"/></svg>Pin</span><span><svg><use href="#i-trash"/></svg>Delete</span><span><svg><use href="#i-pr"/></svg>View pull requests</span><span><svg><use href="#i-rebuild"/></svg>View branch - Commit 6e2e</span></div></div>
          <div class="vsep"></div><div class="disk"><svg><use href="#i-disk"/></svg><div>Used Disk Space<b>627.7 MB</b></div></div><div class="vsep"></div>
          <div class="cta"><span class="btn btn-line">View Project</span><span><svg><use href="#i-hist"/></svg>View older versions</span></div></article>
        <article class="build"><div class="info"><h3>A test for our 5.6 image</h3><span class="date">11/1/2025 6:50 PM</span>
          <div class="acts"><span><svg><use href="#i-rebuild"/></svg>Rebuild</span><span><svg><use href="#i-pin"/></svg>Pin</span><span><svg><use href="#i-trash"/></svg>Delete</span><span><svg><use href="#i-pr"/></svg>View pull requests</span><span><svg><use href="#i-rebuild"/></svg>View branch - Commit 6e2e</span></div></div>
          <div class="vsep"></div><div class="disk"><svg><use href="#i-disk"/></svg><div>Used Disk Space<b>2.1 GB</b></div></div><div class="vsep"></div>
          <div class="cta"><span class="btn btn-line">View Project</span><span><svg><use href="#i-hist"/></svg>View older versions</span></div></article>
        <article class="build"><div class="info"><h3>Testing of PHP 7.0</h3><span class="date">11/1/2025 6:50 PM</span>
          <div class="acts"><span><svg><use href="#i-rebuild"/></svg>Rebuild</span><span><svg><use href="#i-pin"/></svg>Pin</span><span><svg><use href="#i-trash"/></svg>Delete</span><span><svg><use href="#i-pr"/></svg>View pull requests</span><span><svg><use href="#i-rebuild"/></svg>View branch - Commit 6e2e</span></div></div>
          <div class="vsep"></div><div class="disk"><svg><use href="#i-disk"/></svg><div>Used Disk Space<b>569.4 MB</b></div></div><div class="vsep"></div>
          <div class="cta"><span class="btn btn-line">View Project</span><span><svg><use href="#i-hist"/></svg>View older versions</span></div></article>
        <article class="build"><div class="info"><h3>A test for PHP 8.2</h3><span class="date">11/1/2025 6:50 PM</span>
          <div class="acts"><span><svg><use href="#i-rebuild"/></svg>Rebuild</span><span><svg><use href="#i-pin"/></svg>Pin</span><span><svg><use href="#i-trash"/></svg>Delete</span><span><svg><use href="#i-pr"/></svg>View pull requests</span><span><svg><use href="#i-rebuild"/></svg>View branch - Commit 6e2e</span></div></div>
          <div class="vsep"></div><div class="disk"><svg><use href="#i-disk"/></svg><div>Used Disk Space<b>571.3 MB</b></div></div><div class="vsep"></div>
          <div class="cta"><span class="btn btn-line">View Project</span><span><svg><use href="#i-hist"/></svg>View older versions</span></div></article>
        <article class="build"><div class="info"><h3>Testing of PHP 7.0</h3><span class="date">11/1/2025 6:50 PM</span></div>
          <div class="vsep"></div><div class="disk"></div><div class="vsep"></div>
          <div class="cta"><span class="btn btn-line">View Project</span></div></article>
      </div>
    </div>
  </section>

  <p class="abs caption" style="left:123px;top:1577px">Index of Builds</p>
  <p class="abs caption" style="left:884px;top:1577px">Index of Builds</p>

  <!-- ===== Build Details: light ===== -->
  <section class="abs screen light" style="left:123px;top:1612px">
    <aside class="side">
      <div class="brand"><span class="dot"></span>Vexla.IO<svg><use href="#i-chev"/></svg></div>
      <ul class="nav" style="top:46px">
        <li class="on"><svg><use href="#i-stack"/></svg>Builds</li>
        <li><svg><use href="#i-user"/></svg>Build Assets</li>
        <li><svg><use href="#i-upload"/></svg>Upload Tokens</li>
      </ul>
      <div class="usage"><div class="bar"><b></b></div><div class="row">Using 8.6 GB of 500 GB<span class="pill-upgrade">Upgrade</span></div></div>
    </aside>
    <div class="main">
      <div class="topbar"><svg class="mode"><use href="#i-moon"/></svg><span class="user">Welcome, User<i></i></span></div>
      <div class="page-head"><div><h2>Vexla_Test</h2><p class="crumbs">Vexla.IO &gt; VexlaIO_vexla_test &gt; <b>Build details</b></p></div></div>
      <div class="detail-head">
        <div class="info"><h3>Testing PHP 8.5 Container</h3><span class="date">11/1/2025 6:50 PM</span>
          <div class="acts"><span><svg><use href="#i-rebuild"/></svg>Rebuild</span><span><svg><use href="#i-pin"/></svg>Pin</span><span><svg><use href="#i-trash"/></svg>Delete</span><span><svg><use href="#i-pr"/></svg>View pull requests</span><span><svg><use href="#i-rebuild"/></svg>View branch</span></div></div>
        <div class="vsep"></div><div class="disk"><svg><use href="#i-disk"/></svg><div>Used Disk Space<b>627.0 MB</b></div></div>
        <span class="btn btn-fill">View Site</span><div class="vsep"></div>
        <span class="adv"><svg width="7" height="7"><use href="#i-code"/></svg>Advanced Functions</span>
      </div>
      <div class="tasks">
        <article class="task"><div class="th"><div><h4>CodeNest Downloader Task</h4><p class="dur"><svg><use href="#i-clock"/></svg>Duration: <b>1 seconds 154 milliseconds</b></p></div><span class="tog x">×</span></div>
          <ol class="log">
            <li>1 $ mkdir -p /src</li><li>2 $ cd /src</li><li>3 $ source /root/.nvm/nvm.sh</li><li>4 $ mkdir -p /src</li><li>5 $ cd /src</li>
            <li>6 $ wget -q -O - --header 'Authorization: token &lt;******&gt;' https://api.codenest.example/repos/VexlaIO/vexla.io/tarball/839687fe8b7f06206645f818d60</li>
            <li>7 $ tar xzf - --strip-components=1</li><li>8 $ exit</li>
          </ol></article>
        <article class="task"><div class="th"><div><h4>Asset Downloader Task</h4><p class="dur"><svg><use href="#i-clock"/></svg>Duration: <b>852 milliseconds</b></p></div><span class="tog">+</span></div></article>
        <article class="task"><div class="th"><div><h4>Database Task</h4><p class="dur"><svg><use href="#i-clock"/></svg>Duration: <b>27 seconds 730 milliseconds</b></p></div><span class="tog">+</span></div></article>
      </div>
    </div>
  </section>

  <!-- ===== Build Details: dark ===== -->
  <section class="abs screen dark" style="left:884px;top:1612px">
    <aside class="side">
      <div class="brand"><span class="dot"></span>Vexla.IO<svg><use href="#i-chev"/></svg></div>
      <ul class="nav">
        <li class="on"><svg><use href="#i-stack"/></svg>Builds</li>
        <li><svg><use href="#i-user"/></svg>Build Assets</li>
        <li><svg><use href="#i-upload"/></svg>Upload Tokens</li>
      </ul>
      <div class="usage"><div class="bar"><b></b></div><div class="row">Using 8.6 GB of 500 GB<span class="pill-upgrade">Upgrade</span></div></div>
    </aside>
    <div class="main">
      <div class="topbar"><svg class="mode"><use href="#i-sun"/></svg><span class="user">Welcome, User<i></i></span></div>
      <div class="page-head"><div><h2>Vexla_Test</h2><p class="crumbs">Vexla.IO &gt; VexlaIO_vexla_test &gt; <b>Build details</b></p></div></div>
      <div class="detail-head">
        <div class="info"><h3>Testing PHP 8.5 Container</h3><span class="date">11/1/2025 6:50 PM</span>
          <div class="acts"><span><svg><use href="#i-rebuild"/></svg>Rebuild</span><span><svg><use href="#i-pin"/></svg>Pin</span><span><svg><use href="#i-trash"/></svg>Delete</span><span><svg><use href="#i-pr"/></svg>View pull requests</span><span><svg><use href="#i-rebuild"/></svg>View branch</span></div></div>
        <div class="vsep"></div><div class="disk"><svg><use href="#i-disk"/></svg><div>Used Disk Space<b>627.0 MB</b></div></div>
        <span class="btn btn-fill">View Site</span><div class="vsep"></div>
        <span class="adv"><svg width="7" height="7"><use href="#i-code"/></svg>Advanced Functions</span>
      </div>
      <div class="tasks">
        <article class="task"><div class="th"><div><h4>CodeNest Downloader Task</h4><p class="dur"><svg><use href="#i-clock"/></svg>Duration: <b>1 seconds 154 milliseconds</b></p></div><span class="tog x">×</span></div>
          <ol class="log">
            <li>1 $ mkdir -p /src</li><li>2 $ cd /src</li><li>3 $ source /root/.nvm/nvm.sh</li><li>4 $ mkdir -p /src</li><li>5 $ cd /src</li>
            <li>6 $ wget -q -O - --header 'Authorization: token &lt;******&gt;' https://api.codenest.example/repos/VexlaIO/vexla.io/tarball/839687fe8b7f06206645f818d60</li>
            <li>7 $ tar xzf - --strip-components=1</li><li>8 $ exit</li>
          </ol></article>
        <article class="task"><div class="th"><div><h4>Database Task</h4><p class="dur"><svg><use href="#i-clock"/></svg>Duration: <b>27 seconds 730 milliseconds</b></p></div><span class="tog">+</span></div></article>
        <article class="task"><div class="th"><div><h4>Asset Downloader Task</h4><p class="dur"><svg><use href="#i-clock"/></svg>Duration: <b>27 seconds 730 milliseconds</b></p></div><span class="tog">+</span></div></article>
      </div>
    </div>
  </section>

  <p class="abs caption" style="left:123px;top:2049px">Build Details</p>
  <p class="abs caption" style="left:884px;top:2049px">Build Details</p>

</div>
</body>
</html>
```